Med Spa business card design with logo

Need a logo design and business card for our new company Velora Skinworks Med Spa. We are a medical office that deals with high end clients. We offer them skin care products which include NERVAX, lip augmentation, and various laser for the skin. I king of like the logo attached, maybe something along those lines but also open to any logo concept.
Updates

Target Market(s)

Out target audience are male and females in the age range of 21-80 years of age

Industry/Entity Type

Medical

Contact Information for Business Card

woukd like front of card to have logo and business name VELORA SKINWORKS MEDSPA. Back of card employee name and phone number along with instagram logo and user name

Font styles to use
Serif
Sans Serif

Requirements
Must have
• prefer monochromatic look white, black, gold
Should not have
• not too colorful

```html
<!DOCTYPE html>
<html lang="en">
<head>
<meta charset="utf-8">
<title>Velora Skinworks Med Spa — Business Card</title>
<link rel="stylesheet" href="https://fonts.googleapis.com/css2?family=Arimo:wght@400&display=swap">
<style>
  :root {
    --stage: #d9d8da;
    --ink: #000000;
    --paper: #ffffff;
    --silver-light: #c9c8ca;
    --silver-dark: #8f8d90;
    --mark: #b8b7ba;
    --text-dark: #111111;
  }
  * { margin: 0; padding: 0; box-sizing: border-box; }
  html, body {
    width: 1200px; height: 833px; overflow: hidden;
    background: var(--stage);
    font-family: "Arimo", Arial, sans-serif;
  }
  .sheet {
    width: 1200px; height: 833px;
    display: flex; flex-direction: column;
    align-items: center; justify-content: center; gap: 40px;
  }
  .card {
    position: relative;
    width: 600px; height: 343px;
    box-shadow: 0 6px 18px rgba(0,0,0,.18);
    overflow: hidden;
  }
  .card-front {
    background: var(--ink);
    display: flex; align-items: center; justify-content: center; gap: 14px;
  }
  .brand-dot {
    width: 46px; height: 46px; border-radius: 50%;
    background: var(--mark);
    flex: none;
  }
  .brand-name {
    color: var(--paper);
    font-size: 26px; letter-spacing: .5px;
  }
  .card-back .backdrop { position: absolute; inset: 0; }
  .back-brand {
    position: absolute; left: 26px; top: 22px;
    display: flex; align-items: center; gap: 14px;
  }
  .back-brand .brand-dot { width: 58px; height: 58px; }
  .back-brand .brand-name { font-size: 22px; line-height: 1.05; }
  .person {
    position: absolute; left: 42px; top: 172px; color: var(--paper);
  }
  .person-name { font-size: 22px; }
  .person-role { font-size: 13px; margin-top: 8px; }
  .contacts {
    position: absolute; right: 22px; bottom: 20px;
    list-style: none; text-align: right;
    color: var(--text-dark); font-size: 15px; line-height: 21px;
  }
  .contacts li { display: flex; justify-content: flex-end; align-items: center; gap: 8px; }
  .icon { width: 12px; height: 12px; flex: none; }
  .contacts .no-icon { padding-right: 20px; }
</style>
</head>
<body>
<main class="sheet">
  <section class="card card-front">
    <span class="brand-dot"></span>
    <span class="brand-name">VELORA SKINWORKS MEDSPA</span>
  </section>

  <section class="card card-back">
    <svg class="backdrop" viewBox="0 0 600 343" preserveAspectRatio="none" aria-hidden="true">
      <defs>
        <linearGradient id="silver" x1="0" y1="0" x2="1" y2="1">
          <stop offset="0" stop-color="var(--silver-light)"/>
          <stop offset="1" stop-color="var(--silver-dark)"/>
        </linearGradient>
      </defs>
      <rect width="600" height="343" fill="url(#silver)"/>
      <path d="M0,343 C220,230 400,90 540,0 H600 C430,110 250,250 0,343 Z" fill="var(--paper)"/>
      <path d="M0,0 H540 C400,90 220,230 0,330 Z" fill="var(--ink)"/>
    </svg>

    <div class="back-brand">
      <span class="brand-dot"></span>
      <span class="brand-name">VELORA SKINWORKS<br>MEDSPA</span>
    </div>

    <div class="person">
      <div class="person-name">Mara Ellison</div>
      <div class="person-role">Manager</div>
    </div>

    <ul class="contacts">
      <li>415 555 0198
        <svg class="icon" viewBox="0 0 12 12"><rect width="12" height="12" fill="var(--ink)"/><path d="M3,2 L5,2 L5.5,4 L4.5,5 Q6,7.5 7,7.5 L8,6.5 L10,7 L10,9 Q5,10 3,2 Z" fill="var(--paper)"/></svg>
      </li>
      <li>1-541-555-0142
        <svg class="icon" viewBox="0 0 12 12"><rect width="12" height="12" fill="var(--ink)"/><rect x="3" y="5" width="6" height="4" fill="var(--paper)"/><rect x="2.5" y="3" width="7" height="1.5" fill="var(--paper)"/></svg>
      </li>
      <li>hello@velora.com
        <svg class="icon" viewBox="0 0 12 12"><rect width="12" height="12" fill="var(--ink)"/><rect x="2.5" y="3.5" width="7" height="5" fill="var(--paper)"/><path d="M2.5,3.5 L6,6.5 L9.5,3.5" stroke="var(--ink)" fill="none" stroke-width=".8"/></svg>
      </li>
      <li>www.veloraskin.com
        <svg class="icon" viewBox="0 0 12 12"><rect width="12" height="12" fill="var(--ink)"/><rect x="3.5" y="3.5" width="5" height="5" fill="var(--paper)"/></svg>
      </li>
      <li class="no-icon">veloraskinworks</li>
    </ul>
  </section>
</main>
</body>
</html>
```